Food Safety Consultancy Flyer Design

We need a flyer design for a new company called Tundo Training. New food safety regulations are coming into effect for all food operators in March 2016. My company provides training and resources to support food operators during the transition onto the new Food Control Plan. For the designs we would like to see any of the colours used from the logo which is attached. The flyer will be letting operators know that there are new regulations and we are here to help. Our company offers three packages: 1. Videos (training videos) 2. Webinars and Workshop 3. One-on-one mentoring. Our websites main colour used is the green colour from the logo.
Food service operators: cafes, restaurants etc.
Hospitality

```html
<!DOCTYPE html>
<html lang="en">
<head>
<meta charset="utf-8">
<title>Tundo Training – Food Act 2014 Flyer</title>
<link rel="stylesheet" href="https://fonts.googleapis.com/css2?family=Montserrat:wght@400;500;600&family=Roboto+Condensed:ital,wght@0,700;1,400;1,700&family=Open+Sans:wght@400;600;700&display=swap">
<style>
  :root {
    --blue: #1f6db5;
    --footer-blue: #1b67b3;
    --green: #3bb34a;
    --orange: #f6a531;
    --ink: #1e1e1e;
    --grey: #8a8a8a;
    --paper: #ffffff;
    --chef-white: #eef0f2;
    --chef-grey: #cfd3d8;
    --page: #f2f2f2;
  }
  * { box-sizing: border-box; margin: 0; padding: 0; }
  html, body { width: 990px; height: 1200px; overflow: hidden; background: var(--page); }
  .flyer {
    position: relative; width: 990px; height: 1200px; background: var(--paper); overflow: hidden;
    font-family: "Open Sans", Arial, sans-serif; color: var(--ink);
  }

  /* header */
  .act-header { position: absolute; top: 34px; left: 150px; display: flex; align-items: center; gap: 26px; }
  .act-title { font-family: "Montserrat", sans-serif; color: var(--blue); line-height: .95; text-align: center; font-weight: 500; }
  .act-title .act-name { display: block; font-size: 42px; }
  .act-title .act-year { display: block; font-size: 76px; letter-spacing: 1px; }
  .act-divider { width: 2px; height: 110px; background: var(--chef-grey); }
  .act-date { font-family: "Montserrat", sans-serif; }
  .act-date .lead { display: block; font-size: 28px; color: var(--green); }
  .act-date .date { display: block; font-size: 40px; font-weight: 500; margin-top: 4px; white-space: nowrap; }

  .chef { position: absolute; border-radius: 14px; background: linear-gradient(180deg, var(--chef-white), var(--chef-grey)); }
  .chef-left { left: 76px; top: 146px; width: 198px; height: 298px; }
  .chef-right { left: 775px; top: 130px; width: 185px; height: 314px; }
  .chef-pair { left: 680px; top: 870px; width: 265px; height: 262px; }

  /* brand */
  .brand { position: absolute; top: 180px; left: 290px; width: 400px; display: flex; align-items: center; justify-content: center; gap: 20px; }
  .brand-dot { flex: none; border-radius: 50%; background: var(--orange); }
  .brand .brand-dot { width: 60px; height: 60px; }
  .brand-name { font-family: "Montserrat", sans-serif; font-weight: 600; font-size: 58px; line-height: 1.1; color: var(--ink); }
  .brand-name span { display: block; }
  .tagline { position: absolute; top: 372px; left: 0; right: 0; text-align: center; font-family: "Roboto Condensed", sans-serif; font-style: italic; font-weight: 700; font-size: 34px; color: var(--green); }

  /* green band */
  .info-band { position: absolute; top: 458px; left: 46px; right: 0; height: 218px; background: var(--green); border-radius: 8px 0 0 8px; }
  .info-box { position: absolute; top: 8px; left: 8px; right: 30px; height: 88px; background: var(--paper); border-radius: 6px; display: flex; align-items: center; justify-content: center; text-align: center; font-size: 18px; line-height: 1.45; padding: 0 30px; }
  .knowledge { position: absolute; top: 112px; left: 30px; right: 24px; display: flex; gap: 24px; color: var(--paper); }
  .knowledge-lead { font-size: 18px; line-height: 1.45; width: 170px; flex: none; padding-top: 4px; }
  .knowledge-list { font-weight: 600; font-size: 20px; line-height: 1.45; }

  /* heading */
  .help-heading { position: absolute; top: 688px; left: 0; right: 0; height: 44px; display: flex; align-items: center; }
  .help-heading .bar { height: 38px; background: var(--green); }
  .help-heading .bar-left { width: 46px; margin-right: 14px; }
  .help-heading .bar-right { flex: 1; margin-left: 12px; }
  .help-heading h2 { font-family: "Roboto Condensed", sans-serif; font-style: italic; font-weight: 700; font-size: 33px; color: var(--green); white-space: nowrap; }
  .help-heading h2 strong { color: var(--ink); }

  /* packages */
  .package { position: absolute; left: 30px; display: flex; }
  .pkg-icon { width: 150px; text-align: center; flex: none; }
  .pkg-icon .circle { width: 84px; height: 84px; border-radius: 50%; background: var(--green); margin: 0 auto; display: flex; align-items: center; justify-content: center; }
  .pkg-icon .label { display: block; font-family: "Roboto Condensed", sans-serif; font-weight: 700; font-size: 22px; color: var(--green); margin-top: 2px; }
  .pkg-col { font-weight: 700; font-size: 17px; line-height: 1.3; padding: 8px 18px 0; }
  .pkg-col + .pkg-col { border-left: 3px solid var(--green); }
  .col-a { width: 231px; padding-left: 3px; }
  .col-b { width: 251px; }
  .col-c { width: 290px; }
  .pkg-videos { top: 748px; }
  .pkg-workshops { top: 880px; }
  .pkg-mentoring { top: 1018px; }

  .brand-repeat { position: absolute; left: 430px; top: 1030px; display: flex; align-items: center; gap: 12px; font-family: "Montserrat", sans-serif; font-weight: 600; font-size: 28px; line-height: 1.1; color: var(--grey); opacity: .75; }
  .brand-repeat .brand-dot { width: 30px; height: 30px; opacity: .6; }
  .brand-repeat span span { display: block; }

  .footer { position: absolute; left: 0; right: 0; bottom: 0; height: 54px; background: var(--footer-blue); color: var(--paper); display: flex; align-items: center; justify-content: center; font-family: "Roboto Condensed", sans-serif; font-style: italic; font-weight: 700; font-size: 29px; }
  .footer .sep { margin: 0 14px; font-style: normal; font-weight: 400; }
</style>
</head>
<body>
<main class="flyer">
  <header class="act-header">
    <h1 class="act-title"><span class="act-name">Food Act</span><span class="act-year">2014</span></h1>
    <span class="act-divider"></span>
    <p class="act-date"><span class="lead">comes into force on</span><span class="date">1 March 2016</span></p>
  </header>

  <div class="chef chef-left" role="img" aria-label="Illustrated chef holding a ladle and pot"></div>
  <div class="chef chef-right" role="img" aria-label="Illustrated chef holding a serving cloche"></div>

  <div class="brand"><span class="brand-dot"></span><span class="brand-name"><span>Tundo</span><span>Training</span></span></div>
  <p class="tagline">Your reputation is our business</p>

  <section class="info-band">
    <p class="info-box">Food service and food retailers will be on Food Control Plans – documentation of processes and risk management to produce safe and suitable food.</p>
    <div class="knowledge">
      <p class="knowledge-lead">With up-to-date knowledge on:</p>
      <p class="knowledge-list">The Food Act 2014 | &nbsp;Food Control Plan requirements | Verification Expectations | New Food Grading System | New Fees</p>
    </div>
  </section>

  <div class="help-heading">
    <span class="bar bar-left"></span>
    <h2>Let us help you <strong>transition and understand</strong> all there is to know.</h2>
    <span class="bar bar-right"></span>
  </div>

  <section class="package pkg-videos">
    <div class="pkg-icon">
      <span class="circle"><svg width="50" height="36" viewBox="0 0 56 40"><rect x="2" y="10" width="34" height="26" rx="4" fill="#fff"/><polygon points="38,18 54,10 54,36 38,28" fill="#fff"/><circle cx="12" cy="6" r="5" fill="#fff"/><circle cx="26" cy="6" r="5" fill="#fff"/></svg></span>
      <span class="label">Videos</span>
    </div>
    <p class="pkg-col col-a">Animated training videos of the FCP</p>
    <p class="pkg-col col-b">6 month subscription</p>
    <p class="pkg-col col-c">Translated into Mandarin, Japanese, Korean and Hindi</p>
  </section>

  <section class="package pkg-workshops">
    <div class="pkg-icon">
      <span class="circle"><svg width="54" height="44" viewBox="0 0 60 48"><rect x="8" y="16" width="38" height="24" rx="2" fill="none" stroke="#fff" stroke-width="3"/><rect x="2" y="40" width="50" height="4" rx="2" fill="#fff"/><path d="M34 2h22v14H44l-6 5v-5h-4z" fill="#fff"/><circle cx="40" cy="9" r="1.6" fill="#3bb34a"/><circle cx="45" cy="9" r="1.6" fill="#3bb34a"/><circle cx="50" cy="9" r="1.6" fill="#3bb34a"/></svg></span>
      <span class="label">Workshops</span>
    </div>
    <p class="pkg-col col-a">A range of webinars at times to suit the hospitality industry AND half day training workshops.</p>
    <p class="pkg-col col-b">6 month subscription to the video library is included</p>
  </section>

  <section class="package pkg-mentoring">
    <div class="pkg-icon">
      <span class="circle"><svg width="48" height="48" viewBox="0 0 54 54"><circle cx="18" cy="12" r="7" fill="#fff"/><path d="M8 50V30a10 10 0 0 1 20 0v20z" fill="#fff"/><circle cx="38" cy="18" r="6" fill="#fff"/><path d="M30 50V34a8 8 0 0 1 16 0v16z" fill="#fff"/></svg></span>
      <span class="label">Mentoring</span>
    </div>
    <p class="pkg-col col-a">We come to you and go through the FCP page-by-page</p>
  </section>

  <div class="brand-repeat"><span class="brand-dot"></span><span><span>Tundo</span><span>Training</span></span></div>
  <div class="chef chef-pair" role="img" aria-label="Two illustrated chefs holding kitchen utensils"></div>

  <footer class="footer">www.tundotraining.co.nz<span class="sep">|</span>info@tundotraining.co.nz</footer>
</main>
</body>
</html>
```